Nice, modern, and professional credit repair website

We're a new credit repair company and we need a website to inform our prospective clients about the service we provide. We wan't it to catch the attention of the people as well as it be informative of the different types of derogatory items that can be listed on a report. Please refer to ( www.pathtoprime820.net ) for an idea of what I'm looking for.

Coding

Coded - Design and coding required

Number of Pages Required

1 page

Colors
0455a3
0293ce
33a6d7
ffffff

Requirements
Must have
• The website must include information regarding credit repair. We'd like the website to include modern colors similar to that of our logo.
A link to our Friendwall page. Www.friendwall.net/brevmoracreditsolutions
A link to our Instagram page: @BrevmoraCreditSolutions
A link to our Snapchat page: Brevmora-Credit
Also, we'd like to have an area where clients would fill out basic information where we could reach out to them.
Nice to have
• Images of new homes, cars, credit cards (Should NOT endorse Torvi, KP, ZUNO, or Fathomly.)

```html
<!DOCTYPE html>
<html lang="en">
<head>
<meta charset="utf-8">
<title>Brevmora Credit Solutions</title>
<link href="https://fonts.googleapis.com/css2?family=Poppins:wght@400;500;700&family=Lato:wght@400;700&display=swap" rel="stylesheet">
<style>
:root{
  --navy:#0f3e93;
  --blue:#0455a3;
  --sky:#0293ce;
  --sky-soft:#33a6d7;
  --accent:#1b7ec6;
  --ink:#333840;
  --white:#ffffff;
  --footer:#0a1834;
}
*{margin:0;padding:0;box-sizing:border-box}
html,body{width:1200px;height:3858px;overflow:hidden;background:var(--white)}
body{position:relative;font-family:'Lato',sans-serif;color:var(--ink)}
.abs{position:absolute}
.heading{font-family:'Poppins',sans-serif;font-weight:700;color:var(--navy);text-transform:uppercase}
.btn{position:absolute;background:var(--navy);color:var(--white);font-family:'Poppins',sans-serif;display:flex;align-items:center;justify-content:center;text-decoration:none}

/* header */
.site-header{position:absolute;left:0;top:0;width:1200px;height:83px;background:var(--white)}
.brand{position:absolute;left:145px;top:20px;display:flex;align-items:center;gap:10px}
.brand-mark{width:40px;height:40px;border-radius:50%;background:var(--navy)}
.brand-name{font-family:'Poppins',sans-serif;font-weight:700;font-size:21px;color:var(--navy);line-height:1.05}
.brand-name small{display:block;font-size:9px;letter-spacing:2.6px;font-weight:700}
.main-nav{position:absolute;top:34px;font-family:'Poppins',sans-serif;font-size:12.5px;color:#333;text-transform:uppercase}
.main-nav span{position:absolute;white-space:nowrap}
.main-nav .active{color:var(--accent)}
.signup{left:943px;top:21px;width:112px;height:40px;font-size:12.5px}

/* hero */
.hero{position:absolute;left:0;top:83px;width:1200px;height:620px}
.hero-photo{position:absolute;inset:0;background:linear-gradient(180deg,#c9d3cf 0%,#7f9462 22%,#56703a 45%,#3f4a3c 70%,#2f3433 100%);clip-path:polygon(0 0,1200px 0,1200px 534px,835px 612px,432px 532px,0 617px)}
.hero-title{position:absolute;right:143px;top:160px;text-align:right;font-family:'Poppins',sans-serif;font-weight:700;font-size:51px;line-height:55px;color:var(--white);text-shadow:0 2px 6px rgba(0,0,0,.35)}
.hero-cta{left:832px;top:342px;width:223px;height:56px;font-size:20px}
.arrow{position:absolute;top:244px;width:44px;height:44px;border-radius:50%;background:var(--white);display:flex;align-items:center;justify-content:center}

/* welcome */
.welcome-title{left:144px;top:782px;font-size:39px;line-height:56px}
.welcome-text{left:144px;top:962px;width:430px;font-size:15px;line-height:27.3px}
.read-more{left:144px;top:1149px;width:152px;height:48px;font-size:20px;text-transform:uppercase}
.welcome-photo{left:624px;top:781px;width:432px;height:432px;background:linear-gradient(135deg,#8a6f6a 0%,#c77a86 35%,#b05f73 55%,#6f6a78 80%,#4d4646 100%)}

/* services */
.services-band{left:0;top:1301px;width:1200px;height:661px;background:linear-gradient(180deg,#1380c6 0%,#2b8fd6 100%)}
.services-photo{left:0;top:1381px;width:576px;height:689px;background:linear-gradient(140deg,#c6ccd6 0%,#8f98a8 40%,#6f5a4e 60%,#b7bcc6 100%)}
.services-title{left:625px;top:1368px;font-size:40px;color:var(--white)}
.service{position:absolute;left:625px;width:440px;color:var(--white)}
.service svg{position:absolute;left:0;top:2px}
.service h3{position:absolute;left:85px;top:0;font-family:'Poppins',sans-serif;font-weight:400;font-size:24px;white-space:nowrap}
.service p{position:absolute;left:85px;top:37px;width:360px;font-size:11.5px;line-height:19px}

/* blog */
.blog-title{left:0;width:1200px;top:2135px;text-align:center;font-size:40px}
.post{position:absolute;left:0;width:1200px;height:300px}
.post-date{position:absolute;left:144px;top:0;width:64px;text-align:center;font-family:'Poppins',sans-serif;color:var(--accent)}
.post-date .month{display:block;font-size:23px;line-height:30px}
.post-date .day{display:block;font-size:58px;line-height:62px}
.post-photo{position:absolute;left:232px;top:0;width:401px;height:256px}
.post-title{position:absolute;left:665px;top:-8px;width:400px;font-family:'Poppins',sans-serif;font-size:25px;line-height:34px;color:var(--accent);font-weight:400}
.post-text{position:absolute;left:665px;top:78px;width:395px;font-size:15px;line-height:29px}
.post-link{position:absolute;left:667px;top:242px;font-family:'Poppins',sans-serif;font-size:15px;color:var(--navy);text-decoration:underline}
.view-all{left:524px;top:2843px;width:152px;height:49px;font-size:20px}

/* contact */
.contact{left:0;top:2972px;width:1200px;height:428px;background:linear-gradient(120deg,#2c9fd8 0%,#1e86cc 45%,#1576be 100%)}
.contact-title{left:0;width:1200px;top:3040px;text-align:center;font-size:40px;color:var(--white)}
.field{position:absolute;background:var(--white);font-size:13px;color:#555;padding:12px 14px}
.submit{left:559px;top:3274px;width:81px;height:37px;font-size:12px}

/* report */
.report-title{left:0;width:1200px;top:3470px;text-align:center;font-size:40px}
.report-text{left:150px;width:900px;top:3526px;text-align:center;font-size:15px;line-height:27px}
.report-mail{left:0;width:1200px;top:3595px;text-align:center;font-family:'Poppins',sans-serif;font-size:20px;color:var(--navy)}
.email-btn{left:559px;top:3644px;width:81px;height:40px;font-size:12px}

/* footer */
.site-footer{left:0;top:3763px;width:1200px;height:95px;background:var(--footer);color:#9fb4d8;font-size:11.5px}
.footer-links{position:absolute;left:144px;top:24px}
.footer-copy{position:absolute;left:144px;top:57px}
.social{position:absolute;top:26px;font-family:'Lato',sans-serif;font-size:12px;color:#9fb4d8}
</style>
</head>
<body>

<header class="site-header">
  <div class="brand"><span class="brand-mark"></span><span class="brand-name">BREVMORA<small>CREDIT SOLUTIONS</small></span></div>
  <nav class="main-nav">
    <span class="active" style="left:447px">Home</span>
    <span style="left:515px">About Us</span>
    <span style="left:607px">Services</span>
    <span style="left:695px">Pricing</span>
    <span style="left:776px">Blog</span>
    <span style="left:841px">Contact Us</span>
  </nav>
  <a class="btn signup">SIGN UP NOW</a>
</header>

<section class="hero">
  <div class="hero-photo" role="img" aria-label="White SUV driving on a country road through green hills"></div>
  <div class="arrow" style="left:51px"><svg width="16" height="16" viewBox="0 0 16 16"><path d="M11 2 5 8l6 6" fill="none" stroke="#222" stroke-width="2.6"/></svg></div>
  <div class="arrow" style="left:1104px"><svg width="16" height="16" viewBox="0 0 16 16"><path d="M5 2l6 6-6 6" fill="none" stroke="#222" stroke-width="2.6"/></svg></div>
  <h1 class="hero-title">Etiam massa<br>elementum eros<br>tellus venenatis</h1>
  <a class="btn hero-cta">GET STARTED NOW</a>
</section>

<h2 class="abs heading welcome-title">Welcome to<br>Brevmora Credit<br>Solutions</h2>
<p class="abs welcome-text">We specialize in repairing credit reports. It’s our passion. When you sign up today, you can start seeing results in as little as 45 days. We’re ready to answer any questions you may have. Vivamus eleifend vitae nulla vel malesuada. In ac malesuada lacus, et consectetur ante. Fusce vitae lectus sit amet mi pulvinar maximus. Aenean placerat, nibh vel accumsan aliquet,</p>
<a class="btn read-more">Read More</a>
<div class="abs welcome-photo" role="img" aria-label="Close-up of a stack of credit cards on a wooden table"></div>

<section class="abs services-band"></section>
<div class="abs services-photo" role="img" aria-label="Hands typing on a laptop beside printed financial charts"></div>
<h2 class="abs heading services-title">What we do</h2>

<div class="service" style="top:1448px">
  <svg width="70" height="66" viewBox="0 0 70 66" fill="none" stroke="#fff" stroke-width="2"><rect x="2" y="8" width="66" height="56" rx="3"/><line x1="2" y1="20" x2="68" y2="20"/><path d="M14 3v10M28 3v10M42 3v10M56 3v10"/><g stroke-dasharray="2 6"><line x1="10" y1="32" x2="62" y2="32"/><line x1="10" y1="42" x2="62" y2="42"/><line x1="10" y1="52" x2="62" y2="52"/></g></svg>
  <h3>Late Payments</h3>
  <p>Vivamus efficitur ex condimentum, malesuada eros eget, feugiat nibh tellus imperdiet eget gravida.</p>
</div>
<div class="service" style="top:1568px">
  <svg width="70" height="60" viewBox="0 0 70 60" fill="none" stroke="#fff" stroke-width="2"><rect x="2" y="4" width="64" height="44" rx="4"/><line x1="2" y1="14" x2="66" y2="14"/><line x1="2" y1="22" x2="66" y2="22"/><rect x="38" y="30" width="20" height="10"/><line x1="10" y1="32" x2="30" y2="32"/><path d="M6 52h60"/></svg>
  <h3>Collection Accounts</h3>
  <p>Vivamus efficitur ex condimentum, malesuada eros eget, feugiat nibh tellus imperdiet eget gravida.</p>
</div>
<div class="service" style="top:1688px">
  <svg width="70" height="66" viewBox="0 0 70 66" fill="none" stroke="#fff" stroke-width="2"><rect x="26" y="4" width="30" height="44" rx="2"/><line x1="32" y1="14" x2="50" y2="14"/><line x1="32" y1="22" x2="50" y2="22"/><circle cx="41" cy="34" r="6"/><rect x="2" y="36" width="20" height="26" rx="2"/><path d="M12 42v10M12 56v2"/><path d="M22 50h18l14-6 10 4-20 14H22"/></svg>
  <h3>Charge offers</h3>
  <p>Vivamus efficitur ex condimentum, malesuada eros eget, feugiat nibh tellus imperdiet eget gravida.</p>
</div>
<div class="service" style="top:1808px">
  <svg width="70" height="56" viewBox="0 0 70 56" fill="none" stroke="#fff" stroke-width="2"><path d="M12 22 18 6h34l6 16"/><rect x="4" y="22" width="62" height="20" rx="4"/><circle cx="16" cy="32" r="4"/><circle cx="54" cy="32" r="4"/><line x1="26" y1="32" x2="44" y2="32"/><path d="M10 42v8h10v-8M50 42v8h10v-8"/></svg>
  <h3>Repossessions</h3>
  <p>Vivamus efficitur ex condimentum, malesuada eros eget, feugiat nibh tellus imperdiet eget gravida.</p>
</div>

<h2 class="abs heading blog-title">Blog</h2>

<article class="post" style="top:2220px">
  <div class="post-date"><span class="month">May</span><span class="day">25</span></div>
  <div class="post-photo" role="img" aria-label="Two-storey house with lit porch and brick driveway" style="background:linear-gradient(160deg,#3f5a2e 0%,#8e9a94 40%,#6a5a48 70%,#5a5a5e 100%)"></div>
  <h3 class="post-title">Etiam elementum, bibendum tellus venenatis, feugiat massa</h3>
  <p class="post-text">Donec interdum neque pharetra eros faucibus laoreet. Phasellus metus diam, laoreet quis imperdiet sit amet, pharetra dignissim nisi. Proin quis dui at justo interdum facilisis tempor in lorem. Fusce quis rhoncus nisi. Donec venenatis dignissim erat vitae varius.</p>
  <a class="post-link">READ MORE</a>
</article>

<article class="post" style="top:2540px">
  <div class="post-date"><span class="month">May</span><span class="day">25</span></div>
  <div class="post-photo" role="img" aria-label="Hands holding several credit cards" style="background:linear-gradient(135deg,#c9a27c 0%,#d9a84a 35%,#2f4a8a 65%,#23305e 100%)"></div>
  <h3 class="post-title">Pellentesque convallis molestie enim sit amet efficitur</h3>
  <p class="post-text">Donec interdum neque pharetra eros faucibus laoreet. Phasellus metus diam, laoreet quis imperdiet sit amet, pharetra dignissim nisi. Proin quis dui at justo interdum facilisis tempor in lorem. Fusce quis rhoncus nisi. Donec venenatis dignissim erat vitae varius.</p>
  <a class="post-link">READ MORE</a>
</article>

<a class="btn view-all">VIEW ALL</a>

<section class="abs contact" role="img" aria-label="Blue-tinted photo of hands using a laptop and card"></section>
<h2 class="abs heading contact-title" style="color:var(--white)">Contact Us</h2>
<div class="field" style="left:290px;top:3106px;width:217px;height:39px">Name</div>
<div class="field" style="left:513px;top:3106px;width:218px;height:39px">Email</div>
<div class="field" style="left:737px;top:3106px;width:218px;height:39px">Phone</div>
<div class="field" style="left:290px;top:3152px;width:665px;height:104px">Message</div>
<a class="btn submit">SUBMIT</a>

<h2 class="abs heading report-title">Report</h2>
<p class="abs report-text">Fusce vitae lectus sit amet mi pulvinar maximus. Aenean placerat, nibh vel accumsan aliquet, magna nibh accumsan nibh, ac tempus nunc ipsum ac tellus. Cras augue magna, placerat eget nulla non, congue suscipit neque.</p>
<p class="abs report-mail">E-mail us on : info@brevmoracreditsolutions.com</p>
<a class="btn email-btn">EMAIL US</a>

<footer class="abs site-footer">
  <div class="footer-links">Home &nbsp; | &nbsp; About Us &nbsp; | &nbsp; Services &nbsp; | &nbsp; Pricing &nbsp; | &nbsp; Blog &nbsp; | &nbsp; Contact Us</div>
  <div class="footer-copy">Copyright © &nbsp; 2020 &nbsp; Brevmora Credit Solutions. &nbsp; All rights reserved.</div>
  <span class="social" style="left:960px">Friendwall</span>
  <span class="social" style="left:1030px">Chirper</span>
</footer>

</body>
</html>
```